Brimvale Foods Packing Ace the Day

5 Principals for all the team to follow by!

Please can you convert the Ace the day "screenshot 2024-09-08" image into something that has a similair look and feel to the Vision and Values style?

```html
<!DOCTYPE html>
<html lang="en">
<head>
<meta charset="utf-8">
<title>Brimvale Foods Packing – Ace the Day</title>
<link href="https://fonts.googleapis.com/css2?family=Bebas+Neue&family=Poppins:wght@400;600;700;800&display=swap" rel="stylesheet">
<style>
  :root{
    --page:#dedede;
    --white:#ffffff;
    --ink:#222222;
    --charcoal:#2b2b2b;
    --brand-red:#e31e24;
    --brand-green:#5bbd3c;
    --mustard:#d4bc55;
    --burnt-orange:#cc5726;
    --crimson:#b61e22;
    --teal:#55a3b0;
    --navy:#1f2333;
  }
  *{box-sizing:border-box;margin:0;padding:0}
  html,body{width:1000px;height:1200px;overflow:hidden;background:var(--page)}
  body{position:relative;font-family:"Poppins",sans-serif;color:var(--ink)}

  .banner-wrap{position:absolute;left:30px;top:365px;width:940px;height:470px;
    box-shadow:0 12px 24px rgba(0,0,0,.25)}
  .banner{position:absolute;left:0;top:0;width:1340px;height:670px;background:var(--white);
    transform:scale(.70149);transform-origin:0 0;overflow:hidden}

  .frame-shapes{position:absolute;inset:0}

  .brand-name{position:absolute;left:62px;top:42px;height:80px;display:flex;align-items:center;
    font-weight:700;font-size:38px;color:var(--ink);white-space:nowrap}

  .headline{position:absolute;left:655px;top:26px;height:90px;display:flex;align-items:center;gap:16px}
  .headline-title{font-family:"Bebas Neue",sans-serif;font-size:74px;line-height:1;
    color:var(--brand-green);padding-top:8px;white-space:nowrap}
  .headline-tag{font-weight:800;color:var(--white);font-size:27px;line-height:1.08;text-transform:uppercase;white-space:nowrap}

  .grid{position:absolute;left:62px;top:180px;width:1206px;height:444px;
    display:grid;grid-template-columns:repeat(5,241.2px);grid-template-rows:222px 222px}
  .tile{position:relative}
  .tile--mustard{background:var(--mustard)}
  .tile--orange{background:var(--burnt-orange)}
  .tile--crimson{background:var(--crimson)}
  .tile--teal{background:var(--teal)}
  .tile--navy{background:var(--navy)}
  .icon-spot{position:absolute;left:50%;top:50%;width:150px;height:150px;transform:translate(-50%,-50%);
    border-radius:18px;background:rgba(255,255,255,.16)}

  .label{display:flex;flex-direction:column;align-items:center;justify-content:center;text-align:center;padding:0 8px}
  .label-title{font-weight:700;font-size:29px;line-height:1.2}
  .label-sub{font-weight:400;font-size:21px;line-height:1.3}

  .step{position:absolute;top:380px;width:42px;height:42px;margin-left:-21px;border-radius:50%;
    background:var(--white);border:2px solid;display:flex;align-items:center;justify-content:center;
    font-weight:800;font-size:21px;color:var(--ink)}
  .step--1{left:182px;border-color:var(--mustard)}
  .step--2{left:423px;border-color:var(--burnt-orange)}
  .step--3{left:664px;border-color:var(--crimson)}
  .step--4{left:906px;border-color:var(--teal)}
  .step--5{left:1147px;border-color:var(--navy)}
</style>
</head>
<body>
  <div class="banner-wrap">
    <section class="banner">
      <svg class="frame-shapes" viewBox="0 0 1340 670" width="1340" height="670" aria-hidden="true">
        <rect x="0" y="0" width="570" height="9" fill="var(--brand-red)"/>
        <polygon points="555,0 580,0 630,128 608,128" fill="var(--brand-red)"/>
        <polygon points="568,0 1340,0 1340,128 618,128" fill="var(--charcoal)"/>
        <polygon points="100,650 1235,650 1240,670 95,670" fill="var(--charcoal)"/>
        <rect x="0" y="662" width="100" height="8" fill="var(--brand-red)"/>
        <rect x="1237" y="662" width="103" height="8" fill="var(--brand-red)"/>
      </svg>

      <div class="brand-name">Brimvale Foods Packing</div>

      <header class="headline">
        <h1 class="headline-title">THE BRIMVALE WAY..</h1>
        <p class="headline-tag">Ace<br>the Day</p>
      </header>

      <div class="grid">
        <div class="tile tile--mustard"><div class="icon-spot" role="img" aria-label="Icon: hands holding a safety helmet with a tick"></div></div>
        <div class="tile label"><span class="label-title">GMP /<br>Quality</span><span class="label-sub">Drive the<br>Standard</span></div>
        <div class="tile tile--crimson"><div class="icon-spot" role="img" aria-label="Icon: four joined puzzle pieces with hands"></div></div>
        <div class="tile label"><span class="label-title">Plan<br>Attainment</span></div>
        <div class="tile tile--navy"><div class="icon-spot" role="img" aria-label="Icon: process flow of boxes and arrows on a yellow circle"></div></div>

        <div class="tile label"><span class="label-title">H&amp;S</span><span class="label-sub">Call It Out</span></div>
        <div class="tile tile--orange"><div class="icon-spot" role="img" aria-label="Icon: thumbs-up award rosette"></div></div>
        <div class="tile label"><span class="label-title">Team &amp;<br>Behaviors</span><span class="label-sub">What’s Expected<br>of You and<br>Your Team?</span></div>
        <div class="tile tile--teal"><div class="icon-spot" role="img" aria-label="Icon: plan map with clock and flag"></div></div>
        <div class="tile label"><span class="label-title">Process<br>Control</span></div>
      </div>

      <span class="step step--1">1</span>
      <span class="step step--2">2</span>
      <span class="step step--3">3</span>
      <span class="step step--4">4</span>
      <span class="step step--5">5</span>
    </section>
  </div>
</body>
</html>
```